Professional violinist needs business cards

I am trying to attract the following jobs:
-private violin lessons (primarily classical)
-performance gigs (weddings, birthday parties, funerals, etc.)
-collaborations with other artists (studio recordings, performances)

I want to communicate that I have a very high standard of excellence for my work, but I also love people and celebrations.
Values/style words I like are:
love, joy, peace, fun, beauty, authenticity, excellence, warmth, refined/sleek, free spirited. If that's too confusing, just ignore :)

I will attach my favorite business card template that I could find on Canva. The lines are supposed to be like a music staff, which I think is really cool, but I also don't want it to look too busy. I like the simple black and white--I think it looks sharp--but I also am open to other ideas. I also have seen business cards with pictures included that looked great, so I attached an image that could be used as well.

I am also attaching a file that I made of my initials that could be used as a logo, but I'm not sure if it should be included.

Information on the card:
-My name (18 letters total)
-"violinist"
-phone number, email, website

Thank you!

```html
<!DOCTYPE html>
<html lang="en">
<head>
<meta charset="UTF-8">
<title>Rosalind Everhart — Violinist Business Card</title>
<link href="https://fonts.googleapis.com/css2?family=Barlow+Semi+Condensed:wght@400;500;600&family=Barlow+Condensed:wght@400;600&display=swap" rel="stylesheet">
<style>
  :root {
    --backdrop: #d9dadc;
    --card-white: #ffffff;
    --ink: #141414;
    --photo-light: #b9c6cc;
    --photo-mid: #7f939c;
    --photo-dark: #1c2328;
    --on-photo: #ffffff;
    --shadow: rgba(0, 0, 0, 0.18);
  }
  * { margin: 0; padding: 0; box-sizing: border-box; }
  html, body {
    width: 1200px;
    height: 1200px;
    overflow: hidden;
    background: var(--backdrop);
  }
  .sheet {
    width: 1200px;
    height: 1200px;
    display: flex;
    flex-direction: column;
    align-items: center;
    justify-content: center;
    gap: 44px;
  }
  .card {
    position: relative;
    width: 900px;
    height: 514px;
    box-shadow: 0 10px 30px var(--shadow);
    overflow: hidden;
  }

  /* Front */
  .card-front .portrait {
    position: absolute;
    inset: 0;
    background:
      radial-gradient(ellipse at 70% 25%, var(--photo-light) 0%, transparent 55%),
      linear-gradient(150deg, var(--photo-mid) 0%, #5d6f78 40%, #2e3a40 72%, var(--photo-dark) 100%);
  }
  .card-front .identity {
    position: absolute;
    left: 150px;
    bottom: 90px;
    color: var(--on-photo);
  }
  .name {
    font-family: "Barlow Condensed", "Barlow Semi Condensed", sans-serif;
    font-size: 46px;
    line-height: 1;
    text-transform: uppercase;
    letter-spacing: 0.5px;
    white-space: nowrap;
  }
  .name .first { font-weight: 600; }
  .name .last { font-weight: 400; }
  .role {
    font-family: "Barlow Semi Condensed", sans-serif;
    font-weight: 400;
    font-size: 21px;
    letter-spacing: 11px;
    text-transform: uppercase;
    margin-top: 10px;
  }

  /* Back */
  .card-back { background: var(--card-white); color: var(--ink); }
  .card-back .frame {
    position: absolute;
    inset: 40px;
    border: 2px solid var(--ink);
  }
  .card-back .content {
    position: absolute;
    top: 118px;
    left: 0;
    right: 0;
    display: flex;
    align-items: center;
  }
  .card-back .identity {
    width: 430px;
    text-align: right;
    padding-right: 20px;
    padding-top: 80px;
  }
  .card-back .role { margin-top: 6px; letter-spacing: 10px; margin-right: -10px; }
  .divider {
    width: 2px;
    height: 170px;
    background: var(--ink);
  }
  .contacts {
    list-style: none;
    padding-left: 22px;
    display: flex;
    flex-direction: column;
    gap: 12px;
  }
  .contacts li {
    display: flex;
    align-items: center;
    gap: 18px;
    font-family: "Barlow Semi Condensed", sans-serif;
    font-weight: 500;
    font-size: 30px;
    line-height: 1.1;
    white-space: nowrap;
  }
  .contacts svg { width: 30px; height: 30px; flex: none; fill: var(--ink); }
</style>
</head>
<body>
<main class="sheet">

  <section class="card card-front">
    <div class="portrait" role="img" aria-label="Black and white blue-toned portrait of the violinist holding her violin in front of a stone wall"></div>
    <div class="identity">
      <h1 class="name"><span class="first">Rosalind</span> <span class="last">Everhart</span></h1>
      <p class="role">Violinist</p>
    </div>
  </section>

  <section class="card card-back">
    <div class="frame"></div>
    <div class="content">
      <div class="identity">
        <h2 class="name"><span class="first">Rosalind</span> <span class="last">Everhart</span></h2>
        <p class="role">Violinist</p>
      </div>
      <div class="divider"></div>
      <ul class="contacts">
        <li>
          <svg viewBox="0 0 24 24" aria-hidden="true"><path d="M6.6 10.8a15.1 15.1 0 0 0 6.6 6.6l2.2-2.2a1 1 0 0 1 1-.25 11.4 11.4 0 0 0 3.6.57 1 1 0 0 1 1 1V20a1 1 0 0 1-1 1A17 17 0 0 1 3 4a1 1 0 0 1 1-1h3.5a1 1 0 0 1 1 1c0 1.25.2 2.45.57 3.57a1 1 0 0 1-.25 1z"/></svg>
          <span>+00 4821 305 776</span>
        </li>
        <li>
          <svg viewBox="0 0 24 24" aria-hidden="true"><path d="M2 5h20v14H2z M3.5 6.5 12 13l8.5-6.5" fill="var(--ink)"/><path d="M3 6l9 7 9-7" fill="none" stroke="#fff" stroke-width="1.4"/></svg>
          <span>rosalindeverhart@mail.com</span>
        </li>
        <li>
          <svg viewBox="0 0 24 24" aria-hidden="true"><path d="M12 3 2 11.5h3V21h5v-5.5h4V21h5v-9.5h3z"/></svg>
          <span>www.rosalindviolin.com</span>
        </li>
      </ul>
    </div>
  </section>

</main>
</body>
</html>
```